Business Cards - New Logo Rebranding

Hello We know have a red and blue logo and are looking to create new cards. We are looking for the best creativity of the new logo merged with some of the existing artwork provided.

Target Market(s)

Realtors

Industry/Entity Type

Real Estate

Contact Information for Business Card

New logo with rebranded colors

Requirements
Must have
• Creative use of the new logo

```html
<!DOCTYPE html>
<html lang="en">
<head>
<meta charset="utf-8">
<title>Harbor Ridge Inspection Professionals – Business Cards</title>
<link rel="stylesheet" href="https://fonts.googleapis.com/css2?family=Arimo:wght@400;700&display=swap">
<style>
  :root {
    --backdrop: #3d3d3d;
    --brand-blue: #0a6fbd;
    --brand-red: #e2363f;
    --card-white: #ffffff;
    --text-grey: #4a4a4a;
    --text-white: #ffffff;
  }
  * { margin: 0; padding: 0; box-sizing: border-box; }
  html, body { width: 1200px; height: 803px; overflow: hidden; }
  body {
    background: var(--backdrop);
    font-family: "Arimo", Arial, sans-serif;
    position: relative;
  }
  .card {
    position: absolute;
    width: 540px;
    height: 309px;
    border-radius: 22px;
    overflow: hidden;
    border-bottom: 4px solid var(--brand-red);
  }
  .card--contact { left: 330px; top: 70px; background: var(--brand-blue); }
  .card--brand { left: 330px; top: 420px; background: var(--card-white); }

  .contact__emblem {
    position: absolute;
    right: -30px;
    top: -40px;
    width: 300px;
    height: 300px;
  }
  .contact__body {
    position: absolute;
    left: 34px;
    top: 40px;
    color: var(--text-white);
  }
  .wordmark { font-weight: 700; letter-spacing: 1px; line-height: 1; }
  .wordmark__name { font-size: 26px; }
  .wordmark__tag {
    font-size: 8.5px;
    letter-spacing: 1.2px;
    margin-top: 5px;
    padding-bottom: 4px;
    border-bottom: 1.5px solid currentColor;
    display: inline-block;
  }
  .person { margin-top: 44px; }
  .person__name { font-size: 22px; font-weight: 700; }
  .person__title { font-size: 13px; margin-top: 3px; }
  .contact-list { list-style: none; margin-top: 20px; font-size: 13px; line-height: 1.45; }
  .contact-list li { display: flex; align-items: center; gap: 8px; }
  .contact-list .icon { width: 11px; height: 11px; flex: none; }
  .contact-list .spacer { width: 11px; flex: none; }

  .brand__lockup {
    position: absolute;
    left: 0; right: 0;
    top: 62px;
    display: flex;
    flex-direction: column;
    align-items: center;
    color: var(--brand-blue);
  }
  .brand__dot {
    width: 78px; height: 78px;
    border-radius: 50%;
    background: var(--brand-red);
    margin-bottom: 16px;
  }
  .brand__lockup .wordmark__name { font-size: 30px; }
  .brand__lockup .wordmark__tag { font-size: 9.5px; }
  .services {
    position: absolute;
    left: 0; right: 0;
    bottom: 38px;
    text-align: center;
    font-size: 15px;
    color: var(--text-grey);
    letter-spacing: 0.3px;
  }
</style>
</head>
<body>
  <section class="card card--contact">
    <svg class="contact__emblem" viewBox="0 0 300 300" aria-hidden="true">
      <circle cx="150" cy="150" r="140" fill="var(--card-white)" stroke="var(--brand-red)" stroke-width="10"/>
    </svg>
    <div class="contact__body">
      <div class="wordmark">
        <div class="wordmark__name">HARBOR RIDGE</div>
        <div class="wordmark__tag">INSPECTION PROFESSIONALS</div>
      </div>
      <div class="person">
        <div class="person__name">Dana Whitfield</div>
        <div class="person__title">Certified Mold Inspector</div>
      </div>
      <ul class="contact-list">
        <li>
          <svg class="icon" viewBox="0 0 12 12" aria-hidden="true"><path d="M2.5 1 L4.5 1 L5.2 3.6 L3.9 4.6 Q5 7 7.4 8.1 L8.4 6.8 L11 7.5 L11 9.5 Q10.5 11 9 11 Q1 10 1 3 Q1 1.5 2.5 1Z" fill="var(--text-white)"/></svg>
          800.555.0142
        </li>
        <li>
          <svg class="icon" viewBox="0 0 12 12" aria-hidden="true"><rect x="2.5" y="0.5" width="7" height="11" rx="1.2" fill="none" stroke="var(--text-white)" stroke-width="1.2"/><circle cx="6" cy="9.6" r="0.7" fill="var(--text-white)"/></svg>
          562.555.0198
        </li>
        <li><span class="spacer"></span>dana@harborridgeinspect.com</li>
        <li><span class="spacer"></span>www.HarborRidgeInspect.com</li>
      </ul>
    </div>
  </section>

  <section class="card card--brand">
    <div class="brand__lockup">
      <div class="brand__dot"></div>
      <div class="wordmark">
        <div class="wordmark__name">HARBOR RIDGE</div>
      </div>
      <div class="wordmark"><div class="wordmark__tag">INSPECTION PROFESSIONALS</div></div>
    </div>
    <p class="services">HOME • SEWER • MOLD • COMMERCIAL • TERMITE • ROOF</p>
  </section>
</body>
</html>
```